Civic Learning Studio PocketDeck

We are looking for a fresh new look for our famous Signal Sense Handset cards. These cards are used as a pedagogical device by teachers and students to help people critically analyze media messages.

Now that we are in the era of Orvo 12, we would like the Signal Sense Handset to look fresh and new. All the content stays the same, but graphic elements, color and overall design can be changed to look contemporary and modern.

Target Market(s)

Teenagers, young adults, secondary and college teachers

Industry/Entity Type

Education

Colors

Designer to choose colors to be used in the design.

Requirements
Must have
• All the content that is on the current card, with icons and text
Nice to have
• Fresh use of color
• More modern phone design like the smartphones people use today
Should not have
• ...too much black

```html
<!DOCTYPE html>
<html lang="en">
<head>
<meta charset="utf-8">
<title>Civic Learning Studio – Signal Sense Handset Cards</title>
<link rel="stylesheet" href="https://fonts.googleapis.com/css2?family=Montserrat:wght@700;800&family=Questrial&display=swap">
<style>
  :root{
    --backdrop:#4a4748;
    --teal:#1a9bb0;
    --teal-deep:#137f93;
    --yellow:#f2c01e;
    --orange:#f05a28;
    --green:#8cc63f;
    --white:#ffffff;
    --ink:#222222;
    --stamp:#d3d3d3;
    --photo-light:#c9ccce;
    --photo-mid:#9aa6b2;
    --head:'Montserrat', sans-serif;
    --body:'Questrial', sans-serif;
  }
  *{box-sizing:border-box;margin:0;padding:0}
  html,body{width:1200px;height:1200px;overflow:hidden;background:var(--backdrop)}
  .canvas{position:relative;width:1200px;height:1200px}

  .card{position:absolute;width:760px;height:540px;background:var(--white);overflow:hidden;box-shadow:0 10px 24px rgba(0,0,0,.35)}
  .card--front{left:40px;top:40px}
  .card--back{left:400px;top:620px}

  /* Front */
  .front__topband{position:absolute;left:0;top:0;width:100%;height:14px;background:var(--orange)}
  .front__discuss{position:absolute;left:0;top:14px;width:100%;height:280px;background:linear-gradient(90deg,var(--teal-deep),var(--teal))}
  .front__rule{position:absolute;left:0;top:294px;width:100%;height:5px;background:var(--green)}
  .front__media{position:absolute;left:0;top:299px;width:100%;height:179px;background:var(--yellow)}
  .front__orangeline{position:absolute;left:0;top:478px;width:100%;height:4px;background:var(--orange)}
  .front__title{position:absolute;left:28px;top:28px;font:800 30px/1 var(--head);color:var(--white);letter-spacing:.5px}
  .prompt{position:absolute;display:flex;align-items:center;gap:12px;color:var(--white);font:17px/1.15 var(--body)}
  .prompt svg{flex:none;width:30px;height:30px}
  .media-item{position:absolute;width:120px;text-align:center;color:var(--ink);font:18px/1 var(--body)}
  .media-item svg{display:block;margin:0 auto 5px;width:24px;height:24px}
  .portrait{position:absolute;left:462px;top:48px;width:312px;height:312px;border-radius:50%;border:8px solid var(--white);
    background:linear-gradient(160deg,var(--photo-light),var(--photo-mid))}
  .front__footer{position:absolute;left:28px;top:502px;font:15px/1 var(--body);letter-spacing:5px;color:var(--ink)}
  .brand{position:absolute;display:flex;align-items:center;gap:8px;font:700 15px/1 var(--head);color:var(--ink)}
  .brand__mark{width:22px;height:22px;background:var(--teal)}
  .front__brand{right:24px;top:498px}

  /* Back */
  .back__panel{position:absolute;left:0;top:0;width:380px;height:540px}
  .back__phone{position:absolute;top:22px;width:104px;height:196px;border-radius:16px;background:linear-gradient(180deg,#4a4f55,#2a2d31);border:3px solid #9a9a9a}
  .back__phone--one{left:74px}
  .back__phone--two{left:196px}
  .back__title{position:absolute;left:0;width:380px;top:236px;text-align:center;font:800 24px/1.15 var(--head);color:var(--white)}
  .back__underline{position:absolute;left:110px;top:296px;width:160px;height:3px;background:var(--yellow);border-radius:2px}
  .questions{position:absolute;left:22px;top:312px;width:346px;list-style:none}
  .questions li{display:flex;align-items:flex-start;gap:10px;color:var(--white);font:15px/1.2 var(--body);margin-bottom:8px;min-height:34px}
  .questions .num{flex:none;width:26px;height:26px;border-radius:50%;border:2px solid var(--yellow);display:flex;align-items:center;justify-content:center;font:700 12px/1 var(--head)}
  .back__brand{left:400px;top:34px}
  .stamp{position:absolute;right:30px;top:28px;width:78px;height:92px;background:var(--stamp)}
  .address{position:absolute;left:540px;width:190px;height:1.5px;background:var(--ink)}
  .back__url{position:absolute;left:430px;top:488px;font:16px/1 var(--body);color:var(--ink)}
</style>
</head>
<body>
<main class="canvas">

  <section class="card card--front" aria-label="Time to discuss card, front">
    <div class="front__topband"></div>
    <div class="front__discuss"></div>
    <div class="front__rule"></div>
    <div class="front__media"></div>
    <div class="front__orangeline"></div>

    <h1 class="front__title">TIME TO DISCUSS</h1>

    <div class="prompt" style="left:28px;top:74px">
      <svg viewBox="0 0 30 30"><rect x="3" y="3" width="24" height="24" rx="2" fill="#fff"/><path d="M8 15l5 5 9-11" stroke="#1a9bb0" stroke-width="3.5" fill="none"/></svg>Reality Check</div>
    <div class="prompt" style="left:28px;top:122px">
      <svg viewBox="0 0 30 30"><rect x="3" y="8" width="24" height="18" rx="2" fill="none" stroke="#fff" stroke-width="2.5"/><rect x="18" y="14" width="9" height="6" fill="#fff"/><path d="M6 8l12-5 3 5" stroke="#fff" stroke-width="2" fill="none"/></svg>Private Gain or<br>Public Good?</div>
    <div class="prompt" style="left:28px;top:176px">
      <svg viewBox="0 0 30 30"><text x="15" y="27" text-anchor="middle" font-family="Montserrat,sans-serif" font-weight="800" font-size="30" fill="#fff">?</text></svg>What's Left Out?</div>
    <div class="prompt" style="left:28px;top:226px">
      <svg viewBox="0 0 30 30"><rect x="4" y="3" width="22" height="25" fill="none" stroke="#fff" stroke-width="2.5"/><path d="M8 10h4M8 16h4M8 22h4M15 10h7M15 16h7M15 22h7" stroke="#fff" stroke-width="2"/></svg>Values Check</div>

    <div class="prompt" style="left:218px;top:70px">
      <svg viewBox="0 0 30 30"><path d="M3 8h24M3 13h24M3 18h24M3 23h24" stroke="#fff" stroke-width="2.5"/></svg>Read Between the<br>Lines</div>
    <div class="prompt" style="left:218px;top:122px">
      <svg viewBox="0 0 30 30"><path d="M7 22V14a8 8 0 0 1 16 0v8l3 3H4z" fill="#fff"/><circle cx="15" cy="27" r="2.5" fill="#fff"/></svg>Stereotype Alert</div>
    <div class="prompt" style="left:218px;top:170px">
      <svg viewBox="0 0 30 30"><path d="M15 3L28 27H2z" fill="#fff"/><rect x="13.5" y="11" width="3" height="9" fill="#1a9bb0"/><rect x="13.5" y="22" width="3" height="3" fill="#1a9bb0"/></svg>Solutions too Easy</div>
    <div class="prompt" style="left:218px;top:216px">
      <svg viewBox="0 0 30 30"><circle cx="15" cy="15" r="12" fill="none" stroke="#fff" stroke-width="2.5"/><circle cx="15" cy="15" r="8" fill="#fff"/></svg>Record/Save for<br>Later</div>

    <div class="portrait" role="img" aria-label="Photo: young man smiling at his phone"></div>

    <div class="media-item" style="left:16px;top:310px"><svg viewBox="0 0 18 18"><rect x="1" y="3" width="16" height="12" fill="none" stroke="#f05a28" stroke-width="2"/><rect x="4" y="6" width="5" height="4" fill="#f05a28"/></svg>News Media</div>
    <div class="media-item" style="left:16px;top:367px"><svg viewBox="0 0 18 18"><circle cx="4" cy="9" r="2.5" fill="#f05a28"/><circle cx="14" cy="3.5" r="2.5" fill="#f05a28"/><circle cx="14" cy="14.5" r="2.5" fill="#f05a28"/><path d="M4 9L14 3.5M4 9l10 5.5" stroke="#f05a28" stroke-width="1.6"/></svg>Social Media</div>
    <div class="media-item" style="left:16px;top:424px"><svg viewBox="0 0 18 18"><rect x="3" y="1" width="12" height="16" fill="#f05a28"/><rect x="6" y="4" width="6" height="10" fill="#f2c01e"/></svg>Movies</div>

    <div class="media-item" style="left:136px;top:310px"><svg viewBox="0 0 18 18"><rect x="2" y="2" width="3" height="15" fill="#f05a28"/><rect x="7" y="4" width="3" height="13" fill="#f05a28"/><rect x="12" y="2" width="3" height="15" fill="#f05a28"/></svg>Books</div>
    <div class="media-item" style="left:136px;top:367px"><svg viewBox="0 0 18 18"><rect x="1" y="5" width="16" height="9" rx="4.5" fill="#f05a28"/></svg>Video Games</div>
    <div class="media-item" style="left:136px;top:424px"><svg viewBox="0 0 18 18"><rect x="3" y="1" width="12" height="16" rx="1" fill="#f05a28"/></svg>Comics</div>

    <div class="media-item" style="left:256px;top:310px"><svg viewBox="0 0 18 18"><path d="M6 3l10-2v11" stroke="#f05a28" stroke-width="2" fill="none"/><path d="M6 3v11" stroke="#f05a28" stroke-width="2"/><circle cx="4" cy="14" r="3" fill="#f05a28"/><circle cx="14" cy="12" r="3" fill="#f05a28"/></svg>Music</div>
    <div class="media-item" style="left:256px;top:367px"><svg viewBox="0 0 18 18" fill="#f05a28"><rect x="1" y="1" width="4" height="4"/><rect x="7" y="1" width="4" height="4"/><rect x="13" y="1" width="4" height="4"/><rect x="1" y="7" width="4" height="4"/><rect x="7" y="7" width="4" height="4"/><rect x="13" y="7" width="4" height="4"/><rect x="1" y="13" width="4" height="4"/><rect x="7" y="13" width="4" height="4"/><rect x="13" y="13" width="4" height="4"/></svg>Apps</div>
    <div class="media-item" style="left:256px;top:424px"><svg viewBox="0 0 18 18"><rect x="6" y="1" width="6" height="10" rx="3" fill="#f05a28"/><path d="M9 11v6" stroke="#f05a28" stroke-width="2"/></svg>Podcasts</div>

    <div class="media-item" style="left:366px;top:310px"><svg viewBox="0 0 18 18"><rect x="1" y="2" width="16" height="14" fill="#f05a28"/><rect x="1" y="2" width="16" height="3" fill="#c2401a"/></svg>Websites</div>
    <div class="media-item" style="left:366px;top:367px"><svg viewBox="0 0 18 18"><rect x="1" y="5" width="16" height="12" rx="1" fill="none" stroke="#f05a28" stroke-width="2"/><path d="M5 1l4 4 4-4" stroke="#f05a28" stroke-width="1.6" fill="none"/></svg>TV</div>
    <div class="media-item" style="left:366px;top:424px"><svg viewBox="0 0 18 18"><path d="M5 4a7 7 0 1 0 8 0" stroke="#f05a28" stroke-width="2.2" fill="none"/><path d="M9 1v8" stroke="#f05a28" stroke-width="2.2"/></svg>Off</div>

    <p class="front__footer">www.civiclearningstudio.org</p>
    <div class="brand front__brand"><span class="brand__mark"></span>Civic Learning Studio</div>
  </section>

  <section class="card card--back" aria-label="Key questions of media literacy card, back">
    <svg class="back__panel" viewBox="0 0 380 540" aria-hidden="true">
      <defs><linearGradient id="tealFade" x1="0" x2="1"><stop offset="0" stop-color="#1a9bb0"/><stop offset="1" stop-color="#137f93"/></linearGradient></defs>
      <rect width="380" height="540" fill="#f2c01e"/>
      <path d="M0 180 Q150 250 380 140 V540 H0 Z" fill="url(#tealFade)"/>
      <rect y="522" width="380" height="18" fill="#f05a28"/>
    </svg>
    <div class="back__phone back__phone--one" role="img" aria-label="Phone showing the key questions card"></div>
    <div class="back__phone back__phone--two" role="img" aria-label="Phone showing the time to discuss card"></div>

    <h2 class="back__title">KEY QUESTIONS OF<br>MEDIA LITERACY</h2>
    <div class="back__underline"></div>
    <ol class="questions">
      <li><span class="num">1.</span>Who is the author and what is the purpose?</li>
      <li><span class="num">2.</span>What techniques are used to attract and hold your attention?</li>
      <li><span class="num">3.</span>What lifestyles, values and points of view are represented?</li>
      <li><span class="num">4.</span>How might different people interpret the message?</li>
      <li><span class="num">5.</span>What is omitted from the message?</li>
    </ol>

    <div class="brand back__brand"><span class="brand__mark"></span>Civic Learning Studio</div>
    <div class="stamp"></div>
    <div class="address" style="top:262px"></div>
    <div class="address" style="top:292px"></div>
    <div class="address" style="top:322px"></div>
    <p class="back__url">www.civiclearningstudio.org</p>
  </section>

</main>
</body>
</html>
```